Animal Facility Brochure for Pet Boarding, Boutique, Doggie Daycare, Grooming

This brochure is for a Doggie Daycare, Pet Grooming, Dog Boarding & Pet Boutique for the Hollandale Pet Manor & Spa.

Hi there! I am in need of a brochure done for my new up and coming business.
The business will involve Dog/Cat Grooming, Dog Boarding, Doggie Daycare, & a small pet boutique. I am looking for something that stands out and is modern and chic and follows the look of the pictures i have posted (Pippin and Rue) . My color scheme of my business is gray & white. Also i need the brochure to be easily able to understand what we are trying to get across and is easy to read. I am very proud of my logo that was created using sketch hive and would love that incorporated. also i have attached the information that will need to be in the brochure for the client. I am looking for someone who can devote some time working with me on this because this is my first time. I am sure there will need to be some changes so i need someone who is patient. The picture of the projected look of my sign is gearing more towards something clean and modern.

Pet Care

f5f5f5
f8f8f8
dbdbdb
959595
aaaaaa
85abd2
cedeed
eaf1f7

• File nine for Grooming, Boarding, Daycare, Pet Boutique

```html
<!DOCTYPE html>
<html lang="en">
<head>
<meta charset="utf-8">
<title>Hollandale Pet Manor &amp; Spa – Trifold Brochure</title>
<link href="https://fonts.googleapis.com/css2?family=Lato:wght@400;700&family=Cormorant+Garamond:wght@500;600&display=swap" rel="stylesheet">
<style>
  :root{
    --blue:#85abd2;
    --blue-soft:#cedeed;
    --blue-pale:#eaf1f7;
    --white:#ffffff;
    --off-white:#f8f8f8;
    --grey-light:#dbdbdb;
    --grey-mid:#aaaaaa;
    --grey:#959595;
    --ink:#ffffff;
    --stage:#e4e6e9;
  }
  *{box-sizing:border-box;margin:0;padding:0}
  html,body{width:1200px;height:800px;overflow:hidden}
  body{background:var(--stage);font-family:"Lato",sans-serif;color:var(--ink);position:relative}

  .spread{position:absolute;top:176px;width:580px;height:448px;display:flex;box-shadow:0 6px 18px rgba(0,0,0,.18)}
  .spread--inside{left:13px}
  .spread--outside{left:607px}

  .panel{position:relative;width:33.333%;height:100%;overflow:hidden;
    background:linear-gradient(160deg,var(--blue-soft) 0%,var(--blue) 70%);
    padding:12px 11px;font-size:5.6px;line-height:1.42}
  .panel + .panel{border-left:1px solid rgba(255,255,255,.25)}
  .panel--white{background:var(--white);color:var(--grey)}

  .panel h2{font-family:"Lato",sans-serif;font-weight:700;font-size:8.5px;margin:6px 0 3px;letter-spacing:.2px}
  .panel h3{font-weight:700;font-size:7px;margin:5px 0 2px}
  .panel p{margin-bottom:4px;text-align:justify}
  .panel ul{list-style:none;margin-bottom:3px}
  .panel li{padding-left:6px;position:relative;margin-bottom:1.2px}
  .panel li::before{content:"•";position:absolute;left:0}

  .art{position:absolute;background:linear-gradient(135deg,var(--grey-mid),var(--grey))}
  .photo{position:absolute;background:linear-gradient(135deg,#8a7b6a,#c9c2b6 55%,#6e5e4f)}
  .wave{position:absolute;left:0;width:100%}

  /* inside */
  .intro-cat{left:8px;top:8px;width:52px;height:78px;border-radius:26px 26px 8px 8px}
  .intro-text{margin-left:58px;min-height:80px}
  .shield-photo{right:-40px;top:278px;width:128px;height:118px;border:3px solid var(--white);border-radius:8px 8px 64px 64px;background:linear-gradient(135deg,#7b6756,#e9e6e0 60%,#a89a8a)}
  .grooming-text{width:118px}
  .bullet-indent{padding-left:44px}
  .pricing-title{font-size:8px !important;margin-top:0 !important}
  .price-table{width:100%;border-collapse:collapse;font-size:4.6px;margin:4px 0}
  .price-table th{background:var(--grey);font-weight:700;padding:1.5px 2px;text-align:left}
  .price-table td{padding:1.5px 2px;border-bottom:1px solid rgba(255,255,255,.35)}
  .staff-photo{left:20px;right:0;top:238px;height:150px;border-radius:60px 0 0 0;background:linear-gradient(135deg,#d9d6d0,#f4f3f0 50%,#9c948a)}
  .dog-art{left:8px;top:300px;width:58px;height:110px;border-radius:30px 30px 10px 10px}

  /* outside */
  .mission-text{margin-top:60px}
  .shop-photo-left{left:0;right:0;top:318px;bottom:0;background:linear-gradient(135deg,#6c5242,#b79a7b 50%,#3f332b)}
  .cat-art-left{right:6px;top:300px;width:58px;height:110px;border-radius:28px 28px 10px 10px}
  .name-block{font-family:"Cormorant Garamond",serif;font-weight:600;color:var(--white);text-align:center;font-size:11px;line-height:1.15;margin-top:20px;letter-spacing:.4px}
  .hours-title{font-family:"Cormorant Garamond",serif;font-weight:500;font-size:13px;text-align:center;margin:26px 0 10px}
  .hours{text-align:center;font-size:6px}
  .hours dt{font-weight:700;font-size:7px;margin-top:6px}
  .shop-photo-mid{left:0;right:0;top:250px;bottom:0;background:linear-gradient(135deg,#5a4a3f,#d8cfc2 55%,#7d6a5a)}
  .dog-art-mid{left:10px;top:262px;width:70px;height:110px;border-radius:32px 32px 10px 10px}

  .cover-dog-top{left:0;top:0;width:46px;height:62px;border-radius:0 0 28px 0;background:linear-gradient(135deg,var(--blue-soft),var(--blue))}
  .tagline{font-family:"Cormorant Garamond",serif;font-weight:500;font-size:7px;line-height:1.7;text-align:right;color:var(--grey);margin:4px 0 0 50px}
  .cover-name{position:absolute;left:20px;right:20px;top:150px;text-align:center;font-family:"Cormorant Garamond",serif;font-weight:600;font-size:13px;line-height:1.2;color:var(--grey)}
  .cover-name .dot{display:block;width:30px;height:30px;border-radius:50%;background:var(--grey-light);margin:0 auto 10px}
  .cover-dog-bottom{right:0;top:318px;width:70px;height:90px;border-radius:34px 0 0 10px;background:linear-gradient(135deg,var(--blue-soft),var(--blue))}
  .contact{position:absolute;left:11px;bottom:14px;font-size:5.4px;line-height:1.5;color:var(--grey)}
</style>
</head>
<body>

<section class="spread spread--inside" aria-label="Brochure inside spread">
  <article class="panel">
    <div class="art intro-cat" role="img" aria-label="Grey cat silhouette seated on an ornamental swirl"></div>
    <p class="intro-text">Hollandale Pet Manor &amp; Spa is a high-quality, full-service pet facility with personable and nurturing caregivers who will treat your pet like family, giving them the extra care and attention they require and deserve. We are passionate about animals and understand that they all have their own individual personalities and quirks.</p>
    <p>We take the time to get to know your dog or cat and give him or her the individual care your pet needs. We specialize in providing everything for the well-loved pet, including dog daycare, dog and cat boarding, dog and cat grooming and a unique selection of merchandise retail.</p>
    <h2>Grooming</h2>
    <p class="grooming-text">At Hollandale Pet Manor &amp; Spa our experienced grooming staff will take the time to make your pet look fabulous using state-of-the-art grooming equipment and techniques. Our professional groomers are friendly pet lovers who take great pride in their work. Whether you need professional grooming, premium bathing services, or breed standard cuts, our staff will assure your pet walks away from our spa looking his or her best. Grooming and styling are individual spa services and prices will vary depending upon the breed, size, style, condition and temperament of the pet. Hollandale Pet Manor &amp; Spa Groomers are eager to provide a thorough consultation free of charge upon arrival. At this time please express your requests, concerns, and any price questions to your stylist.</p>
    <div class="shield-photo" role="img" aria-label="Photo of the boutique shelves and grooming room in a shield frame"></div>
  </article>

  <article class="panel">
    <h2>Daycare</h2>
    <p>Our dog daycare play rooms are supervised by our trained staff members so that your pet can have a safe place to socialize, exercise, and expend excess energy. We have dedicated playrooms to accommodate different sized guests with different temperaments. We provide your pet with a safe, clean and fun environment that will remind your best friend of home.</p>
    <h3>While your dog is with us...</h3>
    <ul>
      <li>Brand new state of the art suite systems for boarding</li>
      <li>Supervised all levels dog daycare</li>
      <li>We offer 24/7 supervision to ensure a safe, relaxing and comfortable experience with 13 webcams for added security</li>
      <li>Pet Boutique with toys, treats, beds, collars &amp; leashes</li>
      <li>Committed and trained staff to provide the best care</li>
      <li>Equipped with central heat and air conditioning throughout</li>
    </ul>
    <ul class="bullet-indent">
      <li>Elevated beds</li>
      <li>A secure, fenced-in facility</li>
      <li>Wellness checks provided and continuous monitoring of your dog throughout the day</li>
      <li>Opportunities to play and socialize with other dog boarding and daycare guests SAFELY under trained staff supervision</li>
    </ul>
    <h3 class="bullet-indent">While your cat is with us...</h3>
    <ul class="bullet-indent">
      <li>Brand new state of the art kitty condo modular units</li>
      <li>Comfortable bedding for each guest</li>
      <li>Every guest will have playtimes individually</li>
      <li>Your pet will thoroughly enjoy the privacy in their luxurious boarding room away from our canine guests</li>
    </ul>
  </article>

  <article class="panel">
    <h2 class="pricing-title">Pricing &amp; Requirements for Daycare &amp; Boarding</h2>
    <p>We require all guests to complete an evaluation prior to boarding or daycare. This helps our staff determine whether your pet is suited to group play with other dogs and members of our staff.</p>
    <ul>
      <li>Current rabies, distemper and bordetella vaccines required</li>
      <li>All guests must be spayed or neutered</li>
      <li>Flea prevention current before lodging</li>
    </ul>
    <table class="price-table">
      <tr><th>Service</th><th>Single</th><th>Add'l Pet</th><th>Pkg of 10</th></tr>
      <tr><td>Half Day</td><td>$17</td><td>$12</td><td>$150</td></tr>
      <tr><td>Full Day</td><td>$25</td><td>$18</td><td>$220</td></tr>
      <tr><td>Dog Boarding</td><td>$38</td><td>$28</td><td>$340</td></tr>
      <tr><td>Cat Boarding</td><td>$22</td><td>$15</td><td>$190</td></tr>
    </table>
    <div class="photo staff-photo" role="img" aria-label="Photo of the owners seated in the lobby with a spaniel"></div>
    <div class="art dog-art" role="img" aria-label="Grey dog silhouette seated on an ornamental swirl"></div>
  </article>
</section>

<section class="spread spread--outside" aria-label="Brochure outside spread">
  <article class="panel">
    <h2 class="mission-text">Our Mission</h2>
    <p>Is to care for your pet in the best way possible when you are away. We provide a unique social experience for dogs and create a new standard for dog care. Our Kitty condo provides a safe and quiet atmosphere for your kitty. We have set out to create a facility that exemplifies what we ourselves would want for our own best friends. Your pet will have a fun, safe place to play during the day and a secure night time environment when lodging with us. Our staff will go to any lengths to make our guest's stay a true delight. Our professional spa and grooming salon offers a wide range of services for your dog and cat. Our experienced groomers are friendly and knowledgeable and have the expertise to help your pet look and feel its best while exceeding your expectations.</p>
    <div class="photo shop-photo-left" role="img" aria-label="Photo of the pet boutique with leashes and collars on display"></div>
    <svg class="wave" style="top:300px" width="194" height="40" viewBox="0 0 194 40" aria-hidden="true"><path d="M0 40 L0 24 C40 4 90 34 194 10 L194 40 Z" fill="none"/><path d="M0 18 C40 0 90 30 194 4 L194 0 L0 0 Z" fill="#a5c1df"/></svg>
    <div class="art cat-art-left" role="img" aria-label="Grey cat silhouette on a white ornamental swirl"></div>
  </article>

  <article class="panel">
    <p class="name-block">HOLLANDALE PET MANOR<br>&amp; SPA</p>
    <h2 class="hours-title">Hours of Operation</h2>
    <dl class="hours">
      <dt>Monday - Friday</dt><dd>7:30am-6:30pm</dd>
      <dt>Saturday</dt><dd>8:30am-6:30pm</dd>
      <dt>Sunday</dt><dd>10:30am-6:30pm</dd>
    </dl>
    <div class="photo shop-photo-mid" role="img" aria-label="Photo of the boutique interior with shelving and pet beds"></div>
    <div class="art dog-art-mid" role="img" aria-label="Grey dog silhouette on a white ornamental swirl"></div>
  </article>

  <article class="panel panel--white">
    <div class="art cover-dog-top" role="img" aria-label="Blue dog silhouette with ornamental swirl"></div>
    <p class="tagline">When it comes to your pet,<br>we will stop at nothing to<br>keep them healthy,<br>happy &amp; well-loved.</p>
    <p class="cover-name"><span class="dot"></span>HOLLANDALE PET MANOR &amp; SPA</p>
    <div class="art cover-dog-bottom" role="img" aria-label="Blue dog silhouette with ornamental swirl"></div>
    <address class="contact">214 Linden Hollow Road<br>Hollandale, OH 43999<br>www.hollandalepetmanor.com<br>info@hollandalepetmanor.com</address>
  </article>
</section>

</body>
</html>
```